Business Cards for GPS Technology Business - Logo Supplied

Varel Systems Ltd. requires a business card design. Varel is a startup GPS vehicle fleet tracking vendor. Our hardware/software helps business fleets be more productive and reduce operating costs. Our systems utilize a mix of GPS satellite, cell network and web technologies.
We would like to see a double sided original design utilizing our existing logo. Please use whatever colors will work with the blue logo.
As a business, we want to project the image of friendly and approachable lifetime business partners and advisors to our customers - “someone you can trust”. Words customers will use to describe us will include: knowledgeable, supportive, trustworthy and honest.
We will also require Vidplex, Chirpa, Frendly and Lumo+ backgrounds. Winner will be first in line to quote for this work (separate project).
Target Market(s)
Target audience are working owners and managers of vehicle fleets. Usually male, age 30 to 60. Often have a trades background.
Industry/Entity Type
Business
Font styles to use
Requirements
Must have
- Please use the following dummy data for the design:
name: Tim Varel
title: Director
address: 2381 Calden Lane
city: Sommetown, BC
postal code: K7P 2W4
cell phone number: 555-214-7390
business number: 555-318-4602
toll free number: 1-800-555-0193
web site address: www.varel-example.com
tagline: GPS Fleet Tracking Specialists
Nice to have
- Abstract imagery relating to GPS tracking / fleet vehicles / technology
Should not have
- Do not use serif fonts.

```html
<!DOCTYPE html>
<html lang="en">
<head>
<meta charset="utf-8">
<title>Varel Systems – Business Card</title>
<link href="https://fonts.googleapis.com/css2?family=Questrial&display=swap" rel="stylesheet">
<style>
  :root {
    --stage: #1b1b1d;
    --card-white: #f4f5f6;
    --brand-blue: #2a72c0;
    --deep-blue: #1f68b5;
    --shade-blue: #1a5ca8;
    --text-grey: #5a5f66;
    --rule-grey: #b9bcc0;
    --tag-yellow: #f2c21b;
  }
  * { margin: 0; padding: 0; box-sizing: border-box; }
  html, body { width: 1200px; height: 871px; overflow: hidden; }
  body {
    background: var(--stage);
    font-family: "Questrial", "Century Gothic", sans-serif;
    position: relative;
  }
  .card {
    position: absolute;
    width: 560px;
    height: 320px;
    box-shadow: 0 14px 40px rgba(0,0,0,.55);
  }
  .card-front { left: 110px; top: 90px; background: var(--card-white); }
  .card-back { left: 520px; top: 430px; background: var(--deep-blue); overflow: hidden; }

  .brand-name {
    position: absolute; left: 40px; top: 56px;
    font-size: 72px; letter-spacing: 4px;
    color: var(--brand-blue); line-height: 1;
  }
  .person { position: absolute; right: 36px; top: 72px; text-align: right; }
  .person-name { font-size: 22px; color: var(--brand-blue); line-height: 1.2; }
  .person-title { font-size: 15px; color: var(--text-grey); }
  .divider {
    position: absolute; left: 36px; right: 36px; top: 152px;
    border-top: 1px solid var(--rule-grey);
  }
  .contact-list {
    position: absolute; left: 40px; top: 196px; list-style: none;
    font-size: 15px; color: var(--text-grey); letter-spacing: .5px;
  }
  .contact-list li { display: flex; align-items: center; height: 22px; gap: 14px; white-space: nowrap; }
  .contact-list svg { width: 13px; height: 13px; fill: var(--brand-blue); flex: none; }
  .address {
    position: absolute; right: 36px; top: 168px; text-align: right;
    font-size: 14px; line-height: 22px; color: var(--text-grey); white-space: nowrap;
  }

  .back-mark {
    position: absolute; left: -70px; top: 30px;
    width: 290px; height: 290px; border-radius: 50%;
    background: var(--shade-blue);
  }
  .tagline {
    position: absolute; left: 200px; top: 150px;
    font-size: 14px; letter-spacing: 3px; text-transform: uppercase;
    color: var(--tag-yellow); white-space: nowrap;
  }
</style>
</head>
<body>
  <section class="card card-front">
    <div class="brand-name">VAREL</div>
    <div class="person">
      <div class="person-name">Tim Varel</div>
      <div class="person-title">Director</div>
    </div>
    <div class="divider"></div>
    <ul class="contact-list">
      <li><svg viewBox="0 0 16 16" aria-hidden="true"><path d="M3 1l3 3-2 2c1 2 3 4 5 5l2-2 3 3-2 3C7 15 1 9 1 3z"/></svg>555-318-4602</li>
      <li><svg viewBox="0 0 16 16" aria-hidden="true"><rect x="4" y="1" width="8" height="14" rx="1.5"/></svg>555-214-7390</li>
      <li><svg viewBox="0 0 16 16" aria-hidden="true"><path d="M3 1l3 3-2 2c1 2 3 4 5 5l2-2 3 3-2 3C7 15 1 9 1 3z"/></svg>1-800-555-0193</li>
      <li><svg viewBox="0 0 16 16" aria-hidden="true"><circle cx="8" cy="8" r="7"/><path d="M1 8h14M8 1v14" stroke="#f4f5f6" stroke-width="1"/></svg>www.varel-example.com</li>
    </ul>
    <div class="address">2381 Calden Lane<br>Sommetown, BC K7P 2W4</div>
  </section>

  <section class="card card-back">
    <div class="back-mark" aria-hidden="true"></div>
    <div class="tagline">GPS Fleet Tracking Specialists</div>
  </section>
</body>
</html>
```